DELVANE ROOFING YARD SIGN

We need a yard sign to put in our customers' yards when we are roofing their home.
Delvane Roofing
468 Pettigrew Rd
Lake Charles LA 70452
phone: 337-555-0148

Maybe some verbiage like "Your Hometown Roofing Experts"
or
"Family Owned Since 1956"

```html
<!DOCTYPE html>
<html lang="en">
<head>
<meta charset="utf-8">
<title>Delvane Roofing Yard Sign</title>
<link href="https://fonts.googleapis.com/css2?family=Merriweather:wght@700&family=Exo+2:wght@500;600&display=swap" rel="stylesheet">
<style>
  :root {
    --backdrop: #b3b3b3;
    --charcoal: #4a4a4a;
    --ink: #4d4d4d;
    --ink-strong: #333333;
    --paper: #ffffff;
    --tile-dark: #0c1a22;
    --tile-mid: #1d3a4a;
    --tile-edge: #15191c;
  }
  html, body {
    margin: 0;
    padding: 0;
    width: 1200px;
    height: 850px;
    overflow: hidden;
    background: var(--backdrop);
  }
  .yard-sign {
    position: absolute;
    left: 40px;
    top: 145px;
    width: 1120px;
    height: 560px;
    display: block;
  }
  .headline {
    font-family: "Merriweather", Georgia, serif;
    font-weight: 700;
    fill: var(--ink);
    font-size: 100px;
  }
  .brand-name {
    font-family: "Merriweather", Georgia, serif;
    font-weight: 700;
    fill: var(--ink);
    font-size: 44px;
    letter-spacing: 2px;
  }
  .address {
    font-family: "Exo 2", "Arial", sans-serif;
    font-weight: 500;
    fill: var(--paper);
    font-size: 56px;
  }
  .phone-number {
    font-family: "Exo 2", "Arial", sans-serif;
    font-weight: 600;
    fill: var(--ink-strong);
    font-size: 100px;
  }
  .phone-icon { fill: var(--ink-strong); }
</style>
</head>
<body>
<svg class="yard-sign" viewBox="0 0 1781 890" xmlns="http://www.w3.org/2000/svg">
  <defs>
    <linearGradient id="roofTiles" x1="0" y1="0" x2="1" y2="0.3">
      <stop offset="0" stop-color="var(--tile-edge)"/>
      <stop offset="0.35" stop-color="var(--tile-dark)"/>
      <stop offset="0.7" stop-color="var(--tile-mid)"/>
      <stop offset="1" stop-color="var(--tile-dark)"/>
    </linearGradient>
  </defs>

  <!-- sign base -->
  <rect class="sign-base" x="0" y="0" width="1781" height="890" fill="var(--paper)"/>

  <!-- roof photo band -->
  <rect class="roof-photo" x="0" y="0" width="1781" height="262" fill="url(#roofTiles)"
        role="img" aria-label="Photo of dark metal roof tiles"/>

  <!-- gable outline and horizontal band -->
  <polygon class="gable-frame" fill="var(--charcoal)"
           points="0,300 383,40 700,260 1781,260 1781,298 708,298 383,77 0,337"/>

  <!-- white gable and main field -->
  <polygon class="gable-field" fill="var(--paper)"
           points="0,337 383,77 708,298 1781,298 1781,640 0,640"/>

  <!-- brand mark area -->
  <circle class="brand-ring" cx="367" cy="423" r="200" fill="none" stroke="var(--ink)" stroke-width="4"/>
  <text class="brand-name" x="367" y="412" text-anchor="middle">DELVANE</text>
  <text class="brand-name" x="367" y="468" text-anchor="middle">ROOFING</text>

  <!-- headline -->
  <text class="headline" x="1223" y="459" text-anchor="middle">YOUR HOMETOWN</text>
  <text class="headline" x="1223" y="561" text-anchor="middle">ROOFING EXPERTS</text>

  <!-- contact band -->
  <rect class="contact-band" x="0" y="640" width="1781" height="250" fill="var(--charcoal)"/>
  <polygon class="phone-panel" fill="var(--paper)" points="690,890 845,723 1781,723 1781,890"/>

  <text class="address" x="87" y="750">468 Pettigrew Rd</text>
  <text class="address" x="87" y="815">Lake Charles LA 70452</text>

  <!-- phone icon -->
  <g class="phone-icon" transform="translate(814,776)">
    <path d="M10 2 C4 4 0 10 2 18 C6 36 20 52 40 60 C48 62 54 58 56 52 L50 42 C48 40 45 40 43 42 L38 46 C28 42 20 34 16 24 L20 19 C22 17 22 14 20 12 Z"/>
    <path d="M36 14 A14 14 0 0 1 48 26" fill="none" stroke="var(--ink-strong)" stroke-width="4" stroke-linecap="round"/>
    <path d="M38 4 A24 24 0 0 1 58 24" fill="none" stroke="var(--ink-strong)" stroke-width="4" stroke-linecap="round"/>
  </g>
  <text class="phone-number" x="937" y="840">337-555-0148</text>
</svg>
</body>
</html>
```